Sales Page Header Design Project

Hi,
I need a background image created for this sales page: http://quartzventurecamp.example
Width: 977 px
Height: 150 px
Here are a few sample designs to work with: http://harborgrowthinstitute.example/
http://craftingyourlabelweb.example/wp-content/uploads/2011/02/experts1.png
Must be sharp, professional looking and uncluttered.
Colours: Must include blue (I like the blue on the on the current sales page, but will leave shade and colour combinations to your creativity)
Text = Tunde Okafemi Presents
Quartz Venture Camp
Your Blueprint for Building a Profitable, Sustainable Business in Today's Economy!
Any questions, give me a shout
Target Market(s)
Entrepreneurs and Business Owners, aged 21 to 45
Industry/Entity Type
Business
Look and feel
Each slider illustrates characteristics of the customer's brand and the style your logo design should communicate.

```html
<!DOCTYPE html>
<html lang="en">
<head>
<meta charset="utf-8">
<title>Quartz Venture Camp – Header</title>
<link rel="stylesheet" href="https://fonts.googleapis.com/css2?family=Fira+Sans:wght@400;700&family=Noticia+Text&display=swap">
<style>
  :root {
    --bg-dark: #121212;
    --bg-line: #1d1d1d;
    --brand-blue: #2c8cc0;
    --figure-teal: #1f4f5e;
    --text-white: #ffffff;
    --text-soft: #e6e6e6;
  }
  html, body {
    margin: 0;
    padding: 0;
    width: 1200px;
    height: 184px;
    overflow: hidden;
    background: var(--bg-dark);
  }
  .header-banner {
    position: relative;
    width: 1200px;
    height: 184px;
    overflow: hidden;
    background:
      repeating-linear-gradient(
        to bottom,
        var(--bg-line) 0px,
        var(--bg-line) 1px,
        var(--bg-dark) 1px,
        var(--bg-dark) 3px
      );
    text-align: center;
    color: var(--text-white);
  }
  .header-figure {
    position: absolute;
    left: 586px;
    top: 6px;
    width: 30px;
    height: 56px;
    border-radius: 6px;
    background: linear-gradient(to bottom, var(--figure-teal), rgba(31, 79, 94, 0.35));
  }
  .presenter-line {
    position: absolute;
    left: 0;
    right: 0;
    top: 28px;
    margin: 0;
    font-family: "Noticia Text", Georgia, serif;
    font-size: 23px;
    font-weight: 400;
    letter-spacing: 0.3px;
    color: var(--text-white);
  }
  .presenter-name {
    color: var(--brand-blue);
  }
  .program-title {
    position: absolute;
    left: 0;
    right: 0;
    top: 78px;
    margin: 0;
    font-family: "Fira Sans", Arial, sans-serif;
    font-size: 56px;
    font-weight: 700;
    line-height: 1;
    letter-spacing: 0.5px;
    color: var(--text-white);
  }
  .program-title-accent {
    color: var(--brand-blue);
  }
  .program-tagline {
    position: absolute;
    left: 0;
    right: 0;
    top: 150px;
    margin: 0;
    font-family: "Fira Sans", Arial, sans-serif;
    font-size: 15px;
    font-weight: 400;
    color: var(--text-soft);
  }
  .tagline-accent {
    color: var(--brand-blue);
  }
</style>
</head>
<body>
  <header class="header-banner">
    <div class="header-figure" role="img" aria-label="Small teal silhouette of a person raising an arm in celebration"></div>
    <p class="presenter-line"><span class="presenter-name">Tunde Okafemi</span> Presents</p>
    <h1 class="program-title">Quartz Venture <span class="program-title-accent">Camp</span></h1>
    <p class="program-tagline">Your <span class="tagline-accent">Blueprint</span> for Building a Profitable, Sustainable Business in Today’s Economy</p>
  </header>
</body>
</html>
```